Cork Meadow Excursions Post Card/Flyer

Postcard/flyer needs to convey our mission: to provide an authentic, boutique wine tour of exceptional quality with first class customer service. It needs to be clean and high quality. Less is more :) Worthy of 5 star hotel concierges handing them to a guest. I provided an old flyer my friend made and my competitors flyer. Please use these just as reference, but i want to see your creativity. I like the format of "Gentle Harvest" -scan 91-flyer BUT I don't want to copy.

Target Market(s)

Couples, travelers, hotel employees, local industry, etc...

Industry/Entity Type

Boutique

Requirements
Must have
• Must have bullet points of the my previous reference flyer and any photos .Please use website for reference too.
• Vinelist, trip advisor affirmations Plus Instagram
• "Group and Private Tours available"
• "Mention this card for 10% off any tour" - low key please
• corkmeadowexcursions.com, info@corkmeadowexcursions.com, 805-219-6384
Nice to have
• clean lines , simple and elegant
• double sided please
Should not have
• Not too busy.

```html
<!DOCTYPE html>
<html lang="en">
<head>
<meta charset="utf-8">
<title>Cork Meadow Excursions – Flyer</title>
<link rel="stylesheet" href="https://fonts.googleapis.com/css2?family=Lato:ital,wght@0,400;0,700;1,400&family=Marcellus&display=swap">
<style>
  :root {
    --green: #4c6b46;
    --green-dark: #3f5e3a;
    --panel: #f3f4f6;
    --page: #ffffff;
    --rule: #8a9c86;
    --ink: #2a2a2a;
  }
  * { margin: 0; padding: 0; box-sizing: border-box; }
  html, body { width: 1200px; height: 1002px; overflow: hidden; background: var(--page); }
  .flyer { position: relative; width: 1200px; height: 1002px; background: var(--page); font-family: "Lato", sans-serif; color: var(--green); }
  .panel { position: absolute; left: 0; top: 100px; width: 1200px; height: 800px; background: var(--panel); }
  .abs { position: absolute; line-height: 1; white-space: nowrap; }

  .headline { left: 0; width: 1200px; top: 146px; text-align: center; font-family: "Marcellus", serif; font-size: 46px; color: var(--green); }

  .features { position: absolute; left: 38px; top: 238px; width: 550px; list-style: none; font-size: 30px; line-height: 40px; }
  .features li { position: relative; padding-left: 16px; margin-bottom: 17px; }
  .features li::before { content: "·"; position: absolute; left: 0; top: 0; }

  .rule { position: absolute; height: 1px; background: var(--rule); }
  .tours { left: 40px; width: 532px; top: 526px; text-align: center; font-size: 37px; line-height: 47px; white-space: normal; letter-spacing: 0.5px; }

  .photo { position: absolute; }
  .photo--tasting { left: 606px; top: 243px; width: 271px; height: 181px; background: linear-gradient(160deg, #7fa6c9 0%, #4f6f8c 55%, #5c4a3c 100%); }
  .photo--van { left: 891px; top: 243px; width: 271px; height: 181px; background: linear-gradient(170deg, #9fc1e6 0%, #6d8f5b 45%, #a9adb0 100%); }
  .photo--estate { left: 606px; top: 438px; width: 271px; height: 179px; background: linear-gradient(180deg, #5f7a4a 0%, #7f9a5c 55%, #d08a3a 100%); }
  .photo--cellar { left: 891px; top: 438px; width: 271px; height: 179px; background: linear-gradient(180deg, #6b4a2e 0%, #a37a55 50%, #8a6f5c 100%); }

  .badge { position: absolute; left: 148px; top: 676px; }
  .listing { font-weight: 700; color: var(--ink); }
  .listing--one { left: 315px; top: 708px; font-size: 44px; }
  .listing--two { left: 322px; top: 774px; font-size: 38px; }
  .reviews { left: 150px; width: 310px; top: 839px; text-align: center; font-style: italic; font-size: 21px; color: var(--green-dark); }

  .contact-title { left: 607px; top: 668px; font-family: "Marcellus", serif; font-size: 48px; color: var(--green); }
  .social { position: absolute; left: 897px; top: 676px; }
  .contact-line { left: 607px; font-weight: 700; font-size: 26px; color: var(--green); }
  .contact-line--phone { top: 741px; }
  .contact-line--email { top: 781px; }
  .sep { font-weight: 400; color: var(--rule); margin: 0 6px; }
  .offer { left: 607px; top: 837px; font-style: italic; font-size: 21px; color: var(--green-dark); }
</style>
</head>
<body>
<main class="flyer">
  <div class="panel"></div>

  <h1 class="abs headline">An Authentic Wine Tour Experience.</h1>

  <ul class="features">
    <li>Premium wine tasting at boutique wineries</li>
    <li>Safe and comfortable luxury vehicles</li>
    <li>Picnic lunch in a vineyard setting</li>
    <li>Local expert guides</li>
  </ul>

  <div class="rule" style="left:40px;top:517px;width:532px"></div>
  <p class="abs tours">GROUP AND PRIVATE TOURS AVAILABLE</p>
  <div class="rule" style="left:40px;top:618px;width:532px"></div>

  <div class="photo photo--tasting" role="img" aria-label="Guests tasting wine at a lakeside table with a guide"></div>
  <div class="photo photo--van" role="img" aria-label="Silver tour van parked beside a vineyard"></div>
  <div class="photo photo--estate" role="img" aria-label="Winery estate among hills and orange wildflowers"></div>
  <div class="photo photo--cellar" role="img" aria-label="Group of guests in a barrel cellar"></div>

  <svg class="badge" width="148" height="148" viewBox="0 0 148 148" role="img" aria-label="Certificate of excellence award badge">
    <circle cx="74" cy="74" r="72" fill="#ffffff" stroke="#7fb24a" stroke-width="3"/>
  </svg>
  <p class="abs listing listing--one">Vinelist</p>
  <p class="abs listing listing--two">Searchly</p>
  <p class="abs reviews">Over 350 five-star reviews</p>

  <h2 class="abs contact-title">Contact us</h2>
  <svg class="social" width="122" height="32" viewBox="0 0 122 32" role="img" aria-label="Social media links">
    <rect x="0" y="0" width="32" height="32" rx="3" fill="var(--green)"/>
    <rect x="44" y="0" width="32" height="32" rx="3" fill="var(--green)"/>
    <rect x="90" y="0" width="32" height="32" rx="3" fill="var(--green)"/>
  </svg>
  <div class="rule" style="left:607px;top:731px;width:505px"></div>
  <p class="abs contact-line contact-line--phone">805-219-6384<span class="sep">|</span>corkmeadowexcursions.com</p>
  <p class="abs contact-line contact-line--email">info@corkmeadowexcursions.com</p>
  <div class="rule" style="left:607px;top:817px;width:505px"></div>
  <p class="abs offer">Use code: SBCWINE for 10% off any tour</p>
</main>
</body>
</html>
```